Invitation

Please design an invitation for March 31st drop in between 10-1 reception to celebrate the opening of Whitfield's Landing and the Residences at 9 N. Birch. 9 N. Birch Street Quarryville, PA 17504. Tour the buildings newly renovated units and commercial space and enjoy refreshments at the reception.

```html
<!DOCTYPE html>
<html lang="en">
<head>
<meta charset="utf-8">
<title>Grand Opening Invitation – Whitfield's Landing</title>
<link href="https://fonts.googleapis.com/css2?family=Lato:wght@300;400;700&display=swap" rel="stylesheet">
<style>
  :root{
    --page:#ffffff;
    --teal-dark:#106f6a;
    --teal:#0e8a72;
    --green:#14a078;
    --mist:#e6f1ed;
    --ink:#222222;
    --body:#4a4a4a;
    --label:#0f8a6c;
    --white:#ffffff;
  }
  *{margin:0;padding:0;box-sizing:border-box}
  html,body{width:1200px;height:1200px;overflow:hidden;background:var(--page)}
  body{font-family:"Lato",sans-serif;position:relative}
  .flyer{
    position:absolute;left:241px;top:48px;width:684px;height:1050px;
    transform:scale(1.05);transform-origin:0 0;overflow:hidden;
    background:linear-gradient(180deg,var(--mist) 40%,#ffffff 60%,var(--mist) 80%);
  }
  .flyer__shapes{position:absolute;inset:0}
  .brand{
    position:absolute;right:52px;top:520px;
    display:flex;align-items:center;gap:10px;
    font-size:26px;font-weight:400;color:#333;letter-spacing:.5px;
  }
  .brand__mark{width:14px;height:14px;background:var(--teal-dark)}
  .invite{
    position:absolute;left:274px;top:604px;width:362px;
    font-size:17.5px;font-weight:300;line-height:22.8px;color:var(--body);
    text-align:justify;
  }
  .invite strong{font-weight:400;color:var(--ink)}
  .invite p + p{margin-top:22px;text-align:left}
  .thumb{
    position:absolute;left:20px;width:202px;background:var(--white);
    box-shadow:0 3px 5px rgba(0,0,0,.25);padding:6px 6px 0;
  }
  .thumb--lime{top:578px;height:184px}
  .thumb--state{top:795px;height:178px}
  .thumb__photo{display:block;width:190px}
  .thumb--lime .thumb__photo{height:145px;background:linear-gradient(180deg,#b7c6d6 0%,#d9dfe4 28%,#7c7d70 45%,#6d6e62 80%,#2a2829 86%)}
  .thumb--state .thumb__photo{height:144px;background:linear-gradient(180deg,#b9c8d8 0%,#dfe3e7 20%,#83847a 45%,#6e6f66 85%,#b9b6ae 92%)}
  .thumb__label{
    text-align:center;font-size:15px;font-weight:700;color:var(--label);
    line-height:28px;letter-spacing:.2px;
  }
  .contact{position:absolute;left:254px;top:880px;width:420px;color:var(--white)}
  .contact__title{font-size:20px;font-weight:700;margin-bottom:10px}
  .contact__row{display:flex;align-items:flex-start;gap:7px;font-size:15px;line-height:19px}
  .contact__row svg{flex:0 0 14px;margin-top:2px}
  .contact__web{margin-top:14px}
  .contact__phones{position:absolute;left:268px;top:32px}
</style>
</head>
<body>
<div class="flyer">
  <svg class="flyer__shapes" viewBox="0 0 684 1050" width="684" height="1050">
    <defs>
      <linearGradient id="heroFill" x1="0" y1="0" x2="0" y2="1">
        <stop offset="0" stop-color="#9fb3c9"/>
        <stop offset=".22" stop-color="#dde3e8"/>
        <stop offset=".38" stop-color="#8e9089"/>
        <stop offset=".68" stop-color="#6f7066"/>
        <stop offset=".76" stop-color="#b8b6b0"/>
        <stop offset=".82" stop-color="#3a3437"/>
        <stop offset="1" stop-color="#2c2629"/>
      </linearGradient>
      <linearGradient id="waveGreen" x1="0" y1="0" x2="1" y2="0">
        <stop offset="0" stop-color="#119a74"/>
        <stop offset="1" stop-color="#0f8f70"/>
      </linearGradient>
      <linearGradient id="footGreen" x1="0" y1="0" x2="1" y2="1">
        <stop offset="0" stop-color="#12a07a"/>
        <stop offset=".6" stop-color="#0f7f6d"/>
        <stop offset="1" stop-color="#126b68"/>
      </linearGradient>
    </defs>
    <path role="img" aria-label="Rendering of the renovated corner building with wraparound porch under a cloudy sky"
          d="M0 0H684V250C600 330 470 440 300 455C180 465 80 440 0 395Z" fill="url(#heroFill)"/>
    <path d="M0 395C80 440 180 465 300 455C470 440 600 330 684 250V470C560 455 430 480 300 505C180 530 80 560 0 560Z" fill="url(#waveGreen)"/>
    <path d="M0 430C90 480 200 500 320 478C470 450 600 420 684 412V438C560 440 430 470 300 500C180 525 80 530 0 505Z" fill="var(--teal-dark)" opacity=".85"/>
    <path d="M0 560C100 555 200 520 320 490C470 455 600 440 684 438V470C560 455 430 480 300 505C180 530 80 560 0 560Z" fill="var(--green)" opacity=".6"/>
    <path d="M0 860C200 860 420 850 560 830C620 820 660 808 684 800V1050H0Z" fill="url(#footGreen)"/>
  </svg>

  <div class="brand"><span class="brand__mark"></span>Juniper Row Properties</div>

  <figure class="thumb thumb--lime">
    <span class="thumb__photo" role="img" aria-label="Rendering of the building frontage along Birch Street"></span>
    <figcaption class="thumb__label">BIRCH STREET</figcaption>
  </figure>
  <figure class="thumb thumb--state">
    <span class="thumb__photo" role="img" aria-label="Rendering of the building porch along Maple Street"></span>
    <figcaption class="thumb__label">MAPLE STREET</figcaption>
  </figure>

  <div class="invite">
    <p><strong>Juniper Row Properties</strong> invites you to the Grand Opening of <strong>Whitfield's Landing and the Residences</strong>. A Celebration will be held on the 31st of March between 10am to 1pm at <strong>9 N. Birch Street Quarryville, PA 17504.</strong></p>
    <p>Tour the Buildings newly renovated units and commercial space and enjoy refreshments at the venue.</p>
  </div>

  <div class="contact">
    <div class="contact__title">Get in Touch:</div>
    <div class="contact__row">
      <svg width="14" height="16" viewBox="0 0 14 16"><path d="M7 0C3.7 0 1.5 2.4 1.5 5.3 1.5 9 7 16 7 16s5.5-7 5.5-10.7C12.5 2.4 10.3 0 7 0zm0 7.5a2.2 2.2 0 110-4.4 2.2 2.2 0 010 4.4z" fill="#fff"/></svg>
      <span>482 Orchard Pike<br>Quarryville, PA 17504</span>
    </div>
    <div class="contact__row">
      <svg width="14" height="12" viewBox="0 0 14 12"><rect x=".7" y="1.7" width="12.6" height="8.6" fill="none" stroke="#fff" stroke-width="1.2"/><path d="M.7 1.7 7 7l6.3-5.3" fill="none" stroke="#fff" stroke-width="1.2"/></svg>
      <span>info@juniperrowproperties.com</span>
    </div>
    <div class="contact__row contact__web">
      <svg width="14" height="14" viewBox="0 0 14 14"><g fill="none" stroke="#fff" stroke-width="1.1"><circle cx="7" cy="7" r="6.2"/><ellipse cx="7" cy="7" rx="2.8" ry="6.2"/><path d="M.8 7h12.4M1.8 3.8h10.4M1.8 10.2h10.4"/></g></svg>
      <span>www.juniperrowproperties.com</span>
    </div>
    <div class="contact__phones">
      <div class="contact__row">
        <svg width="14" height="14" viewBox="0 0 14 14"><path d="M3 .5 5.2 3 4 5c.9 1.9 2.4 3.4 4.3 4.3l2-1.2 2.5 2.2-1.1 2.3C6.5 12.6 1.4 7.5 1 2.2z" fill="#fff"/></svg>
        <span>717.555.0142</span>
      </div>
      <div class="contact__row">
        <svg width="14" height="14" viewBox="0 0 14 14"><rect x="3.5" y="1" width="7" height="4" fill="#fff"/><rect x="1" y="5" width="12" height="5.5" rx="1" fill="#fff"/><rect x="3.5" y="8.5" width="7" height="4.5" fill="#fff" stroke="#0f8f70" stroke-width="1"/></svg>
        <span>717.555.0187</span>
      </div>
    </div>
  </div>
</div>
</body>
</html>
```